R. Calloway Peril Counsel Business Card

I need a business card that incorporates a two divisions of my company into one business card. The main company or division is R. Calloway Peril Counsel. We have a secondary division of R. Calloway Peril Counsel call Calloway Haulage Cover. I would like this name to be listed as "A Division of R. Calloway Peril Counsel".

Target Market(s)

Customers looking for insurance for their business. WE target businesses with revenues over $5MM

Industry/Entity Type

Business Insurance

Contact Information for Business Card

Use the current logo, but make the R. Calloway Peril Counsel most prevelant over the Calloway Haulage Cover. Name, email, phone number and location

Colors
0054AA
0677BA
7BADD7
CADEEF
E8F1F8

Requirements
Must have
• my current logo
Nice to have
• would like to have "A Division of R. Calloway Peril Counsel" on the card

```html
<!DOCTYPE html>
<html lang="en">
<head>
<meta charset="utf-8">
<title>R. Calloway Peril Counsel – Business Card</title>
<link rel="stylesheet" href="https://fonts.googleapis.com/css2?family=Tinos:ital,wght@0,400;0,700;1,400&display=swap">
<style>
  :root {
    --backdrop: #9a9a9a;
    --navy: #12133f;
    --navy-deep: #0c0d30;
    --pattern-glow: #3a3f8f;
    --white: #ffffff;
    --rule: #8a8ca3;
    --name-grey: #8b8b93;
    --icon: #c9cad6;
  }
  * { margin: 0; padding: 0; box-sizing: border-box; }
  html, body { width: 1200px; height: 1059px; overflow: hidden; }
  body {
    background: var(--backdrop);
    position: relative;
    font-family: "Tinos", "Times New Roman", serif;
    color: var(--white);
  }
  .card {
    position: absolute;
    background: var(--navy);
    border-radius: 28px;
    overflow: hidden;
  }
  .card--front { left: 256px; top: 85px; width: 710px; height: 406px; }
  .card--back  { left: 253px; top: 566px; width: 701px; height: 400px; }

  /* Brand lockups */
  .brand-main {
    position: absolute; left: 46px; top: 60px; width: 266px;
    border-top: 1px solid var(--white); border-bottom: 1px solid var(--white);
    padding: 6px 0 5px; text-align: center;
  }
  .brand-main__name { font-size: 31px; line-height: 1; letter-spacing: 0.5px; }
  .brand-main__sub  { font-size: 13px; letter-spacing: 6.5px; margin-top: 6px; }
  .brand-square {
    position: absolute; left: 326px; top: 50px; width: 100px; height: 100px;
    border: 3px solid var(--white);
  }
  .brand-division {
    position: absolute; left: 460px; top: 59px; width: 204px; text-align: center;
  }
  .brand-division__name {
    border-top: 1px solid var(--white);
    padding-top: 6px; font-size: 22px; line-height: 1; letter-spacing: 3.5px;
  }
  .brand-division__sub {
    font-size: 11px; letter-spacing: 2px; padding: 5px 0 4px;
    border-bottom: 1px solid var(--white);
  }
  .brand-division__note { font-size: 11px; margin-top: 5px; }

  /* Person */
  .person { position: absolute; left: 42px; top: 178px; }
  .person__name { font-size: 27px; font-weight: 700; color: var(--name-grey); }
  .person__title { font-size: 17px; margin-top: 4px; }
  .divider {
    position: absolute; left: 40px; top: 256px; width: 630px; height: 1px;
    background: var(--rule);
  }

  /* Contacts */
  .contact {
    position: absolute; display: flex; align-items: center; gap: 18px;
    font-size: 18px; white-space: nowrap;
  }
  .contact svg { width: 18px; height: 18px; flex: none; fill: var(--icon); }
  .contact em { font-style: italic; }
  .contact--mobile { left: 41px; top: 274px; }
  .contact--email  { left: 41px; top: 301px; }
  .contact--main   { left: 354px; top: 274px; }
  .contact--haul   { left: 354px; top: 301px; }
  .contact--web    { left: 41px; top: 343px; font-size: 17.5px; }

  /* Back */
  .back-field {
    position: absolute; inset: 0;
    background: radial-gradient(ellipse 40% 45% at 47% 50%, var(--pattern-glow), var(--navy) 70%, var(--navy-deep));
  }
  .back-mark {
    position: absolute; left: 500px; top: 252px;
    display: flex; align-items: center; gap: 8px;
  }
  .back-mark__square { width: 18px; height: 18px; border: 2px solid var(--white); }
  .back-mark__name { font-size: 15px; letter-spacing: 1px; }
</style>
</head>
<body>

<section class="card card--front" aria-label="Business card front">
  <div class="brand-main">
    <div class="brand-main__name">R. CALLOWAY</div>
    <div class="brand-main__sub">PERIL COUNSEL</div>
  </div>
  <div class="brand-square" aria-hidden="true"></div>
  <div class="brand-division">
    <div class="brand-division__name">CALLOWAY</div>
    <div class="brand-division__sub">HAULAGE COVER</div>
    <div class="brand-division__note">A Division of R. Calloway Peril Counsel</div>
  </div>

  <div class="person">
    <div class="person__name">Dale Marrow</div>
    <div class="person__title">Founder / CEO</div>
  </div>
  <div class="divider"></div>

  <div class="contact contact--mobile">
    <svg viewBox="0 0 24 24"><path d="M7 1h10a2 2 0 0 1 2 2v18a2 2 0 0 1-2 2H7a2 2 0 0 1-2-2V3a2 2 0 0 1 2-2zm0 3v14h10V4zm5 15.5a1 1 0 1 0 0 2 1 1 0 0 0 0-2z"/></svg>
    <span>404-555-0186</span>
  </div>
  <div class="contact contact--email">
    <svg viewBox="0 0 24 24"><path d="M2 5h20v14H2zm2 2v.5l8 5.5 8-5.5V7l-8 5.2z"/></svg>
    <span>Dale@RCallowayPeril.com</span>
  </div>
  <div class="contact contact--main">
    <svg viewBox="0 0 24 24"><path d="M6.6 10.8a15 15 0 0 0 6.6 6.6l2.2-2.2a1 1 0 0 1 1-.25 11.4 11.4 0 0 0 3.6.57 1 1 0 0 1 1 1V20a1 1 0 0 1-1 1A17 17 0 0 1 3 4a1 1 0 0 1 1-1h3.5a1 1 0 0 1 1 1c0 1.25.2 2.45.57 3.6a1 1 0 0 1-.25 1z"/></svg>
    <span>770-555-0142 <em>R. Calloway Main</em></span>
  </div>
  <div class="contact contact--haul">
    <svg viewBox="0 0 24 24"><path d="M6.6 10.8a15 15 0 0 0 6.6 6.6l2.2-2.2a1 1 0 0 1 1-.25 11.4 11.4 0 0 0 3.6.57 1 1 0 0 1 1 1V20a1 1 0 0 1-1 1A17 17 0 0 1 3 4a1 1 0 0 1 1-1h3.5a1 1 0 0 1 1 1c0 1.25.2 2.45.57 3.6a1 1 0 0 1-.25 1z"/></svg>
    <span>770-555-0177 <em>Haulage Main</em></span>
  </div>
  <div class="contact contact--web">
    <svg viewBox="0 0 24 24"><path d="M12 2a10 10 0 1 0 0 20 10 10 0 0 0 0-20zm0 2a8 8 0 0 1 7.7 6H16a13 13 0 0 0-2-5.7A8 8 0 0 1 12 4zm-2 .3A13 13 0 0 0 8 10H4.3A8 8 0 0 1 10 4.3zM4.3 14H8a13 13 0 0 0 2 5.7A8 8 0 0 1 4.3 14zm9.7 5.7a13 13 0 0 0 2-5.7h3.7a8 8 0 0 1-5.7 5.7zM10 10a11 11 0 0 1 2-4.5 11 11 0 0 1 2 4.5zm0 4h4a11 11 0 0 1-2 4.5 11 11 0 0 1-2-4.5z"/></svg>
    <span>www.RCallowayPerilCounsel.com | www.CallowayHaulageCover.com</span>
  </div>
</section>

<section class="card card--back" aria-label="Business card back">
  <div class="back-field" role="img" aria-label="Repeating embossed brand pattern in deep navy with a soft blue glow"></div>
  <div class="back-mark">
    <div class="back-mark__square" aria-hidden="true"></div>
    <div class="back-mark__name">R. CALLOWAY</div>
  </div>
</section>

</body>
</html>
```